Résumé app needs 1 more template

Hi, I need 1 more template for my résumé app. The résumé app can be used in a browser (https://pagekilnworks.com/resume-app) on an Zelvo / Zelvo Tab (https://apps.velmoro.net/app/id552817306) or on an Brevix (https://store.quintrel.net/store/apps/details?id=com.pagekilnworks.resume). The app lets the user create a résumé. It currently let's the user choose between 3 templates. I need 1 more. Please use the app first so you know how it will work.

Target Market(s)

Users of the app

Colors

Designer to choose colors to be used in the design.

Requirements
Must have
• original
• beautiful
• the resume template contains the data that the user can currently enter in the app (so do NOT design new features like sliders for level of experience etc)

```html
<!DOCTYPE html>
<html lang="en">
<head>
<meta charset="utf-8">
<title>Résumé Template</title>
<link href="https://fonts.googleapis.com/css2?family=Source+Sans+3:wght@400&family=Open+Sans:wght@400&display=swap" rel="stylesheet">
<style>
  :root {
    --accent-red: #fe5354;
    --accent-blue: #4a7ff0;
    --accent-cyan: #4fd1fb;
    --ink: #111111;
    --paper: #ffffff;
    --suit: #222222;
  }
  html, body {
    margin: 0;
    padding: 0;
    overflow: hidden;
    background: var(--paper);
  }
  .resume {
    position: relative;
    width: 927px;
    height: 1200px;
    background: var(--paper);
    overflow: hidden;
    font-family: "Open Sans", sans-serif;
  }
  .bar { position: absolute; }
  .bar--red { background: var(--accent-red); }
  .bar--blue { background: var(--accent-blue); }

  .portrait {
    position: absolute;
    left: 49px; top: 41px;
    width: 165px; height: 247px;
    background: linear-gradient(180deg, var(--accent-red) 0%, var(--accent-red) 58%, var(--suit) 58%, var(--suit) 100%);
  }

  .name {
    position: absolute;
    left: 302px; width: 514px; top: 28px;
    margin: 0;
    text-align: center;
    font-family: "Source Sans 3", sans-serif;
    font-weight: 400;
    font-size: 52px;
    line-height: 64px;
    color: var(--accent-blue);
  }
  .chevron { position: absolute; top: 42px; width: 50px; height: 40px; }

  .field {
    position: absolute;
    box-sizing: border-box;
    border: 2px dotted var(--ink);
    padding: 3px 6px;
    font-size: 18px;
    line-height: 24px;
    color: var(--ink);
  }

  .section-title {
    position: absolute;
    left: 82px;
    margin: 0;
    font-family: "Source Sans 3", sans-serif;
    font-weight: 400;
    font-size: 35px;
    line-height: 40px;
    color: var(--accent-blue);
  }
  .rule {
    position: absolute;
    right: 57px;
    height: 2px;
    background: var(--accent-blue);
  }
</style>
</head>
<body>
<main class="resume">
  <!-- Portrait frame -->
  <div class="portrait" role="img" aria-label="Profile photo placeholder: person in dark suit on red background"></div>
  <div class="bar bar--red" style="left:221px; top:53px; width:7px; height:247px;"></div>
  <div class="bar bar--red" style="left:62px; top:293px; width:166px; height:7px;"></div>

  <!-- Header -->
  <svg class="chevron" style="left:254px;" viewBox="0 0 50 40" aria-hidden="true">
    <polygon points="0,20 18,2 36,20 18,38" fill="var(--accent-cyan)"/>
    <polyline points="28,4 44,20 28,36" fill="none" stroke="var(--accent-blue)" stroke-width="3"/>
  </svg>
  <h1 class="name">Your Name</h1>
  <svg class="chevron" style="left:816px;" viewBox="0 0 50 40" aria-hidden="true">
    <polygon points="0,20 18,2 36,20 18,38" fill="var(--accent-cyan)"/>
    <polyline points="28,4 44,20 28,36" fill="none" stroke="var(--accent-blue)" stroke-width="3"/>
  </svg>
  <div class="bar bar--red" style="left:227px; top:90px; width:643px; height:7px;"></div>

  <!-- Right border -->
  <div class="bar bar--red" style="left:881px; top:109px; width:7px; height:1025px;"></div>

  <div class="field field--about" style="left:245px; top:114px; width:577px; height:170px;">About you</div>

  <!-- Address -->
  <h2 class="section-title" style="top:316px;">Address</h2>
  <div class="rule" style="left:214px; top:346px;"></div>
  <div class="field" style="left:57px; top:360px; width:794px; height:105px;">Add Address</div>

  <!-- Education -->
  <h2 class="section-title" style="top:478px;">Education</h2>
  <div class="rule" style="left:246px; top:508px;"></div>
  <div class="field" style="left:57px; top:522px; width:793px; height:169px;">Add Education</div>

  <!-- Experience -->
  <h2 class="section-title" style="top:701px;">Experience</h2>
  <div class="rule" style="left:258px; top:731px;"></div>
  <div class="field" style="left:57px; top:749px; width:793px; height:169px;">Add Experience</div>

  <!-- Something Else -->
  <h2 class="section-title" style="top:928px;">Something Else</h2>
  <div class="rule" style="left:328px; top:957px;"></div>
  <div class="field" style="left:57px; top:976px; width:793px; height:111px;">Add Something Else</div>

  <!-- Footer -->
  <div class="bar bar--blue" style="left:49px; top:1145px; width:83px; height:7px;"></div>
  <div class="bar bar--red" style="left:157px; top:1145px; width:716px; height:7px;"></div>
</main>
</body>
</html>
```